SUMMER 2017 WORK EXPERIENCE BROCHURE

We need an emailable PDF brochure with details of our Summer English Language and Work Experience Programmes in the UK. Our company is a family run business based in the South East of England, who pride themselves in personal attention to detail and delivering high quality Language Experiences to European students aged 16 plus. We would like the brochure to be bright, eye catching to both parents and older teenage students. It should contain our Company Blue and our logo.
Target Market(s)
European parents of teenage children interested in sending their children to the UK for English Language and Work Experience programmes
Industry/Entity Type
Travel Industry
Requirements
Must have
- Must be bright - eye catching and information must be easily readable. Must include company logo and have strong brand identity. Some images of teenage students having fun outdoors, doing sports, in learning environments. 2 pages. Must include schedule (see attached word document)
Nice to have
- Want it to show the fun element of the programme, it should feel summery and contain some images of beaches or ocean as we are based by the English seaside.
Should not have
- Should not be too conservative or boring. I have uploaded my previous brochure so you can see what type of thing I've had before - but I am looking for something very different to this :-) *** Have removed previous brochure as I am looking for something completely different, not a variation of the old one.

```html
<!DOCTYPE html>
<html lang="en">
<head>
<meta charset="utf-8">
<title>Sample Programme – Summer Work Experience</title>
<link href="https://fonts.googleapis.com/css2?family=Source+Sans+3:wght@400;600;700&family=Luckiest+Guy&display=swap" rel="stylesheet">
<style>
  :root{
    --brand-blue:#1f57a8;
    --tag-blue:#2ea6da;
    --label-blue:#7fc4e6;
    --orange:#f39a2c;
    --ink:#2b2b2b;
    --rule:#2f2f2f;
    --paper:#f2f4f4;
    --sand-light:#ece4d8;
    --sand-deep:#d6c6ae;
  }
  *{box-sizing:border-box;margin:0;padding:0}
  html,body{width:1200px;height:1200px;overflow:hidden;background:#fff}
  body{position:relative;font-family:"Source Sans 3",Arial,sans-serif;color:var(--ink)}
  .page-label{position:absolute;top:140px;width:300px;text-align:center;font-size:64px;font-weight:400;color:#111;font-family:"Source Sans 3",Arial,sans-serif}
  .page-label--one{left:148px}
  .page-label--two{left:728px}

  .page{position:absolute;top:246px;overflow:hidden;background:var(--paper)}
  .page--one{left:0;width:593px;height:842px}
  .page--two{left:603px;width:597px;height:846px}

  .photo{position:absolute;left:0;width:100%}
  .photo--family{top:0;height:400px;background:linear-gradient(180deg,#8fbfe0 0%,#9fc9e2 12%,#1f8aa6 17%,#3cb8a6 25%,#cfe7ea 45%,#e9eef0 75%,var(--paper) 100%)}
  .photo--family::after{content:"";position:absolute;left:235px;top:10px;width:300px;height:370px;border-radius:140px 140px 20px 20px;background:linear-gradient(180deg,rgba(226,178,140,.55),rgba(214,160,120,.35))}
  .photo--sky{top:0;height:120px;background:linear-gradient(180deg,#3e9fe0 0%,#b9dcf2 30%,#ffffff 38%,#2a8fd0 48%,#54c2d6 62%,#bfe3e8 82%,var(--paper) 100%)}
  .photo--sand{bottom:0;height:230px;background:linear-gradient(180deg,var(--paper) 0%,var(--sand-light) 18%,var(--sand-deep) 100%)}
  .photo--sand::after{content:"";position:absolute;left:55px;top:30px;width:240px;height:170px;border-radius:30px;background:linear-gradient(135deg,rgba(240,90,120,.35),rgba(240,200,40,.35) 45%,rgba(60,110,170,.3))}

  .stamp{position:absolute;left:0;top:0;width:245px;height:165px}
  .stamp svg{position:absolute;inset:0}
  .stamp__text{position:absolute;left:34px;top:28px;font-family:"Luckiest Guy",Impact,sans-serif;color:#fff;font-size:27px;line-height:1.08;transform:rotate(-8deg);transform-origin:left top;letter-spacing:.5px}
  .stamp__text span{display:block}
  .stamp__text span:first-child{padding-left:28px}

  .week-tag{position:absolute;left:10px;width:104px;height:20px;background:var(--tag-blue);clip-path:polygon(0 0,84% 0,100% 50%,84% 100%,0 100%);color:#fff;font-weight:700;font-size:14px;line-height:20px;padding-left:7px}

  .day-row{position:absolute;left:0;width:100%;height:20px}
  .day-tag{position:absolute;top:0;width:63px;height:20px;clip-path:polygon(0 0,78% 0,100% 50%,78% 100%,0 100%);background:var(--orange)}
  .day-tag::before{content:"";position:absolute;inset:1.3px;clip-path:polygon(0 0,77% 0,99% 50%,77% 100%,0 100%);background:#fff}
  .day-tag span{position:relative;display:block;padding-left:6px;font-weight:700;font-size:11.5px;line-height:20px;color:var(--orange)}

  .schedule{position:absolute;left:10px;border-collapse:collapse;table-layout:fixed;font-size:11.3px;line-height:1.2}
  .page--one .schedule{width:574px;background:#fff}
  .page--two .schedule{width:577px;background:rgba(255,255,255,.55)}
  .schedule td{border:1.5px solid var(--rule);vertical-align:top;padding:2px 5px;color:#3a3a3a}
  .schedule .slot{background:var(--label-blue);font-weight:700;color:#111}
  .schedule .slot--plain{background:transparent;font-weight:400;color:#3a3a3a}
</style>
</head>
<body>
  <div class="page-label page-label--one">Page 1</div>
  <div class="page-label page-label--two">Page 2</div>

  <!-- Page one -->
  <section class="page page--one">
    <div class="photo photo--family" role="img" aria-label="Photo of a smiling family posing together on a sunny beach"></div>
    <div class="photo photo--sand" role="img" aria-label="Photo of striped flip-flops and a snorkel mask on the sand"></div>

    <div class="stamp">
      <svg viewBox="0 0 245 165" aria-hidden="true"><path d="M0 30 C40 10 120 0 238 0 L230 40 C222 80 200 105 160 125 C120 145 60 160 0 165 Z" fill="var(--brand-blue)"/></svg>
      <div class="stamp__text"><span>Sample</span><span>Programme</span></div>
    </div>

    <div class="week-tag" style="top:386px">Week 1</div>
    <div class="day-row" style="top:414px">
      <div class="day-tag" style="left:80px"><span>SUN</span></div>
      <div class="day-tag" style="left:149px"><span>MON</span></div>
      <div class="day-tag" style="left:218px"><span>TUE</span></div>
      <div class="day-tag" style="left:288px"><span>WED</span></div>
      <div class="day-tag" style="left:358px"><span>THUR</span></div>
      <div class="day-tag" style="left:436px"><span>FRI</span></div>
      <div class="day-tag" style="left:512px"><span>SAT</span></div>
    </div>
    <table class="schedule" style="top:439px">
      <colgroup><col style="width:69px"><col style="width:70px"><col style="width:69px"><col style="width:69px"><col style="width:71px"><col style="width:78px"><col style="width:75px"><col style="width:73px"></colgroup>
      <tr style="height:61px"><td class="slot">AM</td><td>Arrivals at Southmere Airport</td><td>Induction Meeting followed by</td><td></td><td></td><td></td><td></td><td></td></tr>
      <tr style="height:61px"><td class="slot slot--plain">Work Placements</td><td>Work Placements</td><td>Work Placements</td><td>Work Placements</td><td>Work Placements</td><td>Camping and Tree Climbing Experience</td><td></td><td></td></tr>
      <tr style="height:32px"><td class="slot">PM</td><td></td><td>Work Placements</td><td>Work Placements</td><td>Work Placements</td><td>Work Placements</td><td>Transfer to camp site</td><td></td></tr>
      <tr style="height:33px"><td class="slot slot--plain">Evening</td><td></td><td></td><td>Evening activity</td><td></td><td>Evening activity</td><td>Overnight at campsite</td><td></td></tr>
    </table>
  </section>

  <!-- Page two -->
  <section class="page page--two">
    <div class="photo photo--sky" role="img" aria-label="Photo of a tropical sea and sky horizon"></div>
    <div class="photo photo--sand" role="img" aria-label="Photo of striped flip-flops and a snorkel mask on the sand"></div>

    <div class="week-tag" style="top:74px">Week 2</div>
    <div class="day-row" style="top:102px">
      <div class="day-tag" style="left:80px"><span>SUN</span></div>
      <div class="day-tag" style="left:149px"><span>MON</span></div>
      <div class="day-tag" style="left:218px"><span>TUE</span></div>
      <div class="day-tag" style="left:288px"><span>WED</span></div>
      <div class="day-tag" style="left:358px"><span>THUR</span></div>
      <div class="day-tag" style="left:438px"><span>FRI</span></div>
      <div class="day-tag" style="left:513px"><span>SAT</span></div>
    </div>
    <table class="schedule" style="top:129px">
      <colgroup><col style="width:69px"><col style="width:70px"><col style="width:69px"><col style="width:70px"><col style="width:70px"><col style="width:80px"><col style="width:75px"><col style="width:74px"></colgroup>
      <tr style="height:74px"><td class="slot">AM</td><td>Camping and transfers back to Worthing</td><td>Work Placements</td><td>Work Placements</td><td>Work Placements</td><td>Work Placements</td><td>Work Placements</td><td>Day Trip to London</td></tr>
    </table>
    <table class="schedule" style="top:223px">
      <colgroup><col style="width:69px"><col style="width:70px"><col style="width:69px"><col style="width:70px"><col style="width:70px"><col style="width:80px"><col style="width:75px"><col style="width:74px"></colgroup>
      <tr style="height:33px"><td class="slot">PM</td><td></td><td>Work Placements</td><td>Work Placements</td><td>Work Placements</td><td>Work Placements</td><td>Afternoon activity</td><td></td></tr>
      <tr style="height:33px"><td class="slot slot--plain">Evening</td><td></td><td></td><td>Evening activity</td><td></td><td>Evening activity</td><td></td><td></td></tr>
    </table>

    <div class="week-tag" style="top:300px">Week 3</div>
    <div class="day-row" style="top:328px">
      <div class="day-tag" style="left:80px"><span>SUN</span></div>
      <div class="day-tag" style="left:149px"><span>MON</span></div>
      <div class="day-tag" style="left:218px"><span>TUE</span></div>
      <div class="day-tag" style="left:288px"><span>WED</span></div>
      <div class="day-tag" style="left:358px"><span>THUR</span></div>
      <div class="day-tag" style="left:438px"><span>FRI</span></div>
      <div class="day-tag" style="left:513px"><span>SAT</span></div>
    </div>
    <table class="schedule" style="top:357px">
      <colgroup><col style="width:69px"><col style="width:70px"><col style="width:69px"><col style="width:70px"><col style="width:70px"><col style="width:80px"><col style="width:75px"><col style="width:74px"></colgroup>
      <tr style="height:34px"><td class="slot">AM</td><td>Free day</td><td>Work Placements</td><td>Work Placements</td><td>Work Placements</td><td>Work Placements</td><td>Work Placements</td><td>Day Trip to Portsmouth</td></tr>
    </table>
    <table class="schedule" style="top:410px">
      <colgroup><col style="width:69px"><col style="width:70px"><col style="width:69px"><col style="width:70px"><col style="width:70px"><col style="width:80px"><col style="width:75px"><col style="width:74px"></colgroup>
      <tr style="height:33px"><td class="slot">PM</td><td></td><td>Work Placements</td><td>Work Placements</td><td>Work Placements</td><td>Work Placements</td><td>Afternoon activity</td><td></td></tr>
      <tr style="height:34px"><td class="slot slot--plain">Evening</td><td></td><td></td><td>Evening activity</td><td></td><td>Evening activity</td><td></td><td></td></tr>
    </table>

    <div class="week-tag" style="top:486px">Week 4</div>
    <div class="day-row" style="top:514px">
      <div class="day-tag" style="left:80px"><span>SUN</span></div>
      <div class="day-tag" style="left:149px"><span>MON</span></div>
      <div class="day-tag" style="left:218px"><span>TUE</span></div>
      <div class="day-tag" style="left:288px"><span>WED</span></div>
      <div class="day-tag" style="left:358px"><span>THUR</span></div>
      <div class="day-tag" style="left:438px"><span>FRI</span></div>
      <div class="day-tag" style="left:513px"><span>SAT</span></div>
    </div>
    <table class="schedule" style="top:545px">
      <colgroup><col style="width:69px"><col style="width:70px"><col style="width:69px"><col style="width:70px"><col style="width:70px"><col style="width:80px"><col style="width:75px"><col style="width:74px"></colgroup>
      <tr style="height:33px"><td class="slot">AM</td><td>Free day</td><td>Work Placements</td><td>Work Placements</td><td>Work Placements</td><td>Work Placements</td><td>Work Placements</td><td>Departures</td></tr>
      <tr style="height:33px"><td class="slot">PM</td><td></td><td>Work Placements</td><td>Work Placements</td><td>Work Placements</td><td>Work Placements</td><td>Certificate</td><td></td></tr>
      <tr style="height:34px"><td class="slot slot--plain">Evening</td><td></td><td></td><td>Evening activity</td><td></td><td>Evening activity</td><td></td><td></td></tr>
    </table>
  </section>
</body>
</html>
```